RW Frameworks Inc Business cards

We need business cards using our existing logo but slightly modified. Right now the logo says RW Framework Masonry. We want to keep the RW part of the design, but replace the Framework Masonry portion with "FRAMEWORKS". Please see the attached file.
Ideally this would be a blank template so we can add Different Names, titles, and phone numbers later.
On the one side we want only the logo and on the other side the detail. I'm attaching an example for you to see.
Please reach out with any other questions. Our address and other details will be given out once we find a design we like.

Target Market(s)

Construction Industry

```html
<!DOCTYPE html>
<html lang="en">
<head>
<meta charset="utf-8">
<title>RW Frameworks Inc – Business Cards</title>
<link href="https://fonts.googleapis.com/css2?family=Arimo:wght@400;700&display=swap" rel="stylesheet">
<style>
  :root {
    --stage: #2a2a2a;
    --brand-blue: #1273bf;
    --paper: #ffffff;
    --ink: #222222;
    --rule: #9a9a9a;
  }
  * { margin: 0; padding: 0; box-sizing: border-box; }
  html, body { width: 1200px; height: 1200px; overflow: hidden; }
  body {
    background: var(--stage);
    font-family: "Arimo", Arial, sans-serif;
    display: flex;
    flex-direction: column;
    align-items: center;
    justify-content: center;
    gap: 60px;
  }
  .card {
    position: relative;
    width: 900px;
    height: 514px;
    border-radius: 36px;
    overflow: hidden;
  }
  .card--front {
    background: var(--brand-blue);
    display: flex;
    align-items: center;
    justify-content: center;
  }
  .wordmark {
    display: flex;
    align-items: center;
    gap: 16px;
    font-weight: 700;
    letter-spacing: 0.12em;
  }
  .wordmark__square { width: 22px; height: 22px; background: currentColor; }
  .card--front .wordmark { color: var(--paper); font-size: 56px; }

  .card--back { background: var(--paper); }
  .card--back .wordmark {
    position: absolute;
    left: 310px;
    top: 120px;
    color: var(--brand-blue);
    font-size: 44px;
  }
  .person {
    position: absolute;
    right: 470px;
    top: 262px;
    text-align: right;
  }
  .person__name { color: var(--brand-blue); font-weight: 700; font-size: 36px; letter-spacing: 0.01em; }
  .person__title { color: var(--ink); font-size: 22px; margin-top: 2px; }
  .divider {
    position: absolute;
    left: 452px;
    top: 248px;
    width: 2px;
    height: 96px;
    background: var(--rule);
  }
  .contacts {
    position: absolute;
    left: 478px;
    top: 246px;
    list-style: none;
    color: var(--ink);
    font-size: 22px;
    line-height: 33px;
  }
  .contacts li { display: flex; align-items: center; gap: 10px; }
  .contacts svg { width: 16px; height: 16px; fill: var(--brand-blue); flex: none; }
  .address-band {
    position: absolute;
    left: 0;
    right: 0;
    top: 392px;
    height: 64px;
    background: var(--brand-blue);
    color: var(--paper);
    font-size: 24px;
    display: flex;
    align-items: center;
    padding-left: 300px;
  }
</style>
</head>
<body>
  <section class="card card--front" aria-label="Card front">
    <div class="wordmark"><span class="wordmark__square"></span><span>RW FRAMEWORKS</span></div>
  </section>

  <section class="card card--back" aria-label="Card back">
    <div class="wordmark"><span class="wordmark__square"></span><span>RW FRAMEWORKS</span></div>

    <div class="person">
      <p class="person__name">DARREN COLE</p>
      <p class="person__title">Owner/CEO</p>
    </div>

    <div class="divider"></div>

    <ul class="contacts">
      <li>
        <svg viewBox="0 0 16 16" aria-hidden="true"><path d="M3.6 1.5l2.3 2.6-1.3 1.8c.9 2 2.5 3.6 4.5 4.5l1.8-1.3 2.6 2.3-1.4 2.1C7 13.3 2.7 9 1.5 3z"/></svg>
        <span>555-018-2270</span>
      </li>
      <li>
        <svg viewBox="0 0 16 16" aria-hidden="true"><path d="M1 3h14v10H1z M1.8 3.8L8 9l6.2-5.2" stroke="#fff" stroke-width="1.2"/></svg>
        <span>info@rwframeworks.com</span>
      </li>
      <li>
        <svg viewBox="0 0 16 16" aria-hidden="true"><circle cx="8" cy="8" r="7"/><path d="M1 8h14M8 1c-3 3.5-3 10.5 0 14M8 1c3 3.5 3 10.5 0 14" stroke="#fff" stroke-width="1" fill="none"/></svg>
        <span>www.rwframeworks.com</span>
      </li>
    </ul>

    <div class="address-band">1400 W Harlan Avenue Brookfield 6120</div>
  </section>
</body>
</html>
```